Tanning Lotion package label & Logo

Need hot new label for tanning lotion focusing on dark tanning. Sexy design must compete with soon to be dated but still popular "Mabel in the jar" styles here:
http://www.shopvelder.example/s/ref=nb_sb_noss_1?url=search-alias%3Daps&field-keywords=tanning%20lotion&sprefix=tanni%2Caps&rh=i%3Aaps%2Ck%3Atanning%20lotion
Have 30 days to complete. High end product needs right look.
Product name: SunMostGlo
Target Market(s)
SunMostGlo is a high-end, one-of-a-kind, multi-purpose hybrid tanning lotion that can be used indoors as a self-tanner, outdoors on the beach, or at tanning salons. The SunMostGlo formula delivers a high performing silicone base to provide an excellent, non-irritating, non-oily, non-tacky, luxurious, light and greaseless overall feel on the skin when applied. This high performing silicon base also provides sebum absorption and control to help clear and prevent breakouts. SunMostGlo contains a complex mixture of moisturizers and emollients including vitamin B5 to prevent and treat dry skin, protect sensitive skin, and improve skin tone and texture. It also contains a powerful blend of antioxidants including Grape Seed extract which is rich in OPC’s and has 20 times the antioxidant power of vitamin C, and 50 times the antioxidant power of vitamin E to help fight free radicals, protect and improve skin appearance and maintain healthy looking skin. SunMostGlo contains a unique combination of two natural skin-tanning compounds to produce an even, deeper, and longer lasting tan. Tanning accelerators using natural amino acids help increase the production of melanin for a quicker and darker tan. SunMostGlo is the most technologically advanced tanning lotion on the market today!
SunMostGlo is a high-end product and will have a retail price point around $50 USD for 200 ml.
SunMostGlo is aimed at the mid to high market
Target demographic are white girls and women aged 16-49, followed by white males aged 18-55.
SunMostGlo will be sold online direct to consumers initially then followed by;
1. On shelves in beach area shops
2. In tanning salons
3. On shelves in mid-large box retail stores
Industry/Entity Type
Product
Look and feel

```html
<!DOCTYPE html>
<html lang="en">
<head>
<meta charset="utf-8">
<title>SunMostGlo — Advanced Tanning Lotion Label</title>
<link rel="stylesheet" href="https://fonts.googleapis.com/css2?family=Oranienbaum&family=Marcellus&display=swap">
<style>
  :root {
    --backdrop: #ededed;
    --backdrop-edge: #dadada;
    --ink: #110d06;
    --gold-light: #fbe08a;
    --gold-mid: #d9a42a;
    --gold-deep: #7a4a0a;
    --parchment-light: #f1e4c8;
    --parchment-deep: #d8bd8e;
    --flourish-red: #d0141c;
  }
  html, body {
    margin: 0;
    width: 1200px;
    height: 857px;
    overflow: hidden;
  }
  body {
    background: radial-gradient(ellipse at center, #fbfbfb 0%, var(--backdrop) 62%, var(--backdrop-edge) 100%);
  }
  .label-canvas {
    display: block;
    width: 1200px;
    height: 857px;
  }
  .brand-name {
    font-family: "Oranienbaum", "Times New Roman", serif;
    font-size: 66px;
    fill: var(--ink);
    stroke: var(--ink);
    stroke-width: 1.4px;
  }
  .product-line,
  .vitamin-line,
  .quality-line {
    font-family: "Marcellus", "Times New Roman", serif;
    fill: var(--ink);
  }
  .product-line { font-size: 16px; }
  .vitamin-line { font-size: 19px; }
  .quality-line { font-size: 21px; }
</style>
</head>
<body>
<svg class="label-canvas" viewBox="0 0 1200 857" xmlns="http://www.w3.org/2000/svg">
  <defs>
    <linearGradient id="gold" x1="0" y1="0" x2="1" y2="1">
      <stop offset="0" stop-color="var(--gold-light)"/>
      <stop offset="0.45" stop-color="var(--gold-mid)"/>
      <stop offset="0.72" stop-color="var(--gold-deep)"/>
      <stop offset="1" stop-color="var(--gold-light)"/>
    </linearGradient>
    <radialGradient id="gold-soft" cx="0.45" cy="0.4" r="0.65">
      <stop offset="0" stop-color="var(--gold-light)"/>
      <stop offset="0.55" stop-color="var(--gold-mid)"/>
      <stop offset="1" stop-color="var(--gold-deep)"/>
    </radialGradient>
    <radialGradient id="parchment" cx="0.5" cy="0.4" r="0.7">
      <stop offset="0" stop-color="var(--parchment-light)"/>
      <stop offset="1" stop-color="var(--parchment-deep)"/>
    </radialGradient>
    <radialGradient id="flourish-tone" cx="0.5" cy="0.5" r="0.5">
      <stop offset="0" stop-color="var(--flourish-red)" stop-opacity="0.55"/>
      <stop offset="0.6" stop-color="var(--flourish-red)" stop-opacity="0.25"/>
      <stop offset="1" stop-color="var(--flourish-red)" stop-opacity="0"/>
    </radialGradient>
  </defs>

  <!-- side scrollwork (behind the oval) -->
  <path class="scroll-left" role="img" aria-label="Gold acanthus scrollwork ornament, left side"
        d="M338 285 C300 300 272 350 278 430 C284 510 292 560 318 598 C350 606 372 580 380 540 L380 300 C370 288 355 282 338 285 Z"
        fill="url(#gold-soft)" stroke="var(--ink)" stroke-width="3"/>
  <path class="scroll-right" role="img" aria-label="Gold acanthus scrollwork ornament, right side"
        d="M862 285 C900 300 928 350 922 430 C916 510 908 560 882 598 C850 606 828 580 820 540 L820 300 C830 288 845 282 862 285 Z"
        fill="url(#gold-soft)" stroke="var(--ink)" stroke-width="3"/>

  <!-- backing oval -->
  <ellipse class="backing-oval" cx="600" cy="445" rx="292" ry="362"
           fill="var(--ink)" stroke="url(#gold)" stroke-width="9"/>

  <!-- bottom scrollwork -->
  <path class="scroll-bottom-left" role="img" aria-label="Gold scrollwork ornament, lower left"
        d="M400 688 C440 690 500 700 560 716 L548 790 C500 780 450 760 418 735 C404 720 398 705 400 688 Z"
        fill="url(#gold-soft)" opacity="0.95"/>
  <path class="scroll-bottom-right" role="img" aria-label="Gold scrollwork ornament, lower right"
        d="M800 688 C760 690 700 700 640 716 L652 790 C700 780 750 760 782 735 C796 720 802 705 800 688 Z"
        fill="url(#gold-soft)" opacity="0.95"/>

  <!-- rods linking the medallion -->
  <path class="medallion-rod" d="M470 152 C520 138 680 138 730 152" fill="none" stroke="url(#gold)" stroke-width="10" stroke-linecap="round"/>

  <!-- shield frame -->
  <path class="shield-frame"
        d="M352 192 C400 200 450 225 490 225 C540 222 560 172 600 168 C640 172 660 222 710 225 C750 225 800 200 848 192 C815 260 800 300 805 380 C808 470 830 560 868 618 C810 630 760 660 700 720 C660 760 620 790 600 810 C580 790 540 760 500 720 C440 660 390 630 332 618 C370 560 392 470 395 380 C400 300 385 260 352 192 Z"
        fill="url(#gold)" stroke="var(--ink)" stroke-width="4"/>
  <path class="shield-field"
        d="M378 212 C420 220 460 240 492 242 C545 240 565 192 600 188 C635 192 655 240 708 242 C740 240 780 220 822 212 C795 270 782 310 786 380 C790 470 808 550 838 604 C790 616 742 648 688 704 C650 744 618 770 600 786 C582 770 550 744 512 704 C458 648 410 616 362 604 C392 550 410 470 414 380 C418 310 405 270 378 212 Z"
        fill="url(#parchment)" stroke="var(--ink)" stroke-width="3"/>

  <!-- crown medallion -->
  <circle class="crown-medallion" cx="600" cy="92" r="62" fill="url(#gold)" stroke="var(--ink)" stroke-width="4"/>
  <circle cx="600" cy="92" r="47" fill="var(--ink)"/>
  <ellipse class="crown-emblem" role="img" aria-label="Gold crown emblem" cx="600" cy="104" rx="38" ry="26" fill="url(#gold-soft)"/>

  <!-- red flourishes -->
  <ellipse class="flourish-top" role="img" aria-label="Red calligraphic flourish" cx="600" cy="318" rx="106" ry="26" fill="url(#flourish-tone)"/>
  <ellipse class="flourish-bottom" role="img" aria-label="Red calligraphic flourish" cx="600" cy="552" rx="128" ry="32" fill="url(#flourish-tone)"/>

  <!-- wording -->
  <text class="brand-name" x="602" y="424" text-anchor="middle" textLength="264" lengthAdjust="spacingAndGlyphs">SUNMOSTGLO</text>
  <line class="brand-rule" x1="467" y1="435" x2="737" y2="435" stroke="var(--ink)" stroke-width="3"/>
  <text class="product-line" x="600" y="467" text-anchor="middle" textLength="256" lengthAdjust="spacingAndGlyphs">ADVANCED TANNING LOTION</text>
  <text class="vitamin-line" x="600" y="503" text-anchor="middle" textLength="254" lengthAdjust="spacingAndGlyphs">WITH VITAMIN B, C &amp; E</text>
  <text class="quality-line" x="600" y="656" text-anchor="middle" textLength="176" lengthAdjust="spacingAndGlyphs">100% QUALITY</text>
</svg>
</body>
</html>
```